qm - website template
website of specialist in neurosurgery, and teacher at the University in Milan
qm - website template - Education
Creative Brief
Education
Benedetto L. Caramuzza, MD (specialist in neurosurgery and in the history of medicine), historian and anthropologist, teaches history of medicine and health in the Faculty of Medicine, University of Velmora Castrene, where he directs the Institute for anatomical inquiry into past doctrines "(www.dulrota.it).
He's the author of over 250 papers in national and international partner to the history of medical and health disciplines and pharmacological institute of the Italian Ombrilla.
Traditional
blu (see attached logo file)
red (see attached logo file)
We need the graphic template of: • Homepage • Generic content page (text+image+ eventual document to download) • listing page of books + page with information about the selected book • listing page of conference + page with information about the selected conference • Contact The site must be optimized for 1024X768. For the main menu, it's possibile to use not system font. File must be preferably png (adobe fireworks), otherwise ai (adobe illustrator) or psd (adobe photoshop).

```html
<!DOCTYPE html>
<html lang="it">
<head>
<meta charset="utf-8">
<title>Benedetto L. Caramuzza – Home</title>
<link rel="stylesheet" href="https://fonts.googleapis.com/css2?family=Cabin:wght@400;600;700&family=PT+Sans:wght@400;700&display=swap">
<style>
:root{
  --page-top:#f1f2f3;
  --page-mid:#dfe3e7;
  --blue-deep:#1c5f93;
  --blue:#2d7bb5;
  --blue-light:#4a95c9;
  --text-grey:#5a5f66;
  --red:#8e1b22;
  --red-dark:#6d1217;
  --red-line:#a8323a;
  --white:#ffffff;
  --slide-a:#f7f8f9;
  --slide-b:#c9ced3;
}
*{margin:0;padding:0;box-sizing:border-box}
html,body{width:1200px;height:816px;overflow:hidden}
body{
  position:relative;
  font-family:"PT Sans",Arial,sans-serif;
  background:linear-gradient(180deg,var(--page-top) 0,var(--page-mid) 480px,var(--blue-light) 560px,var(--blue) 680px,var(--blue-deep) 816px);
}
.main-nav{position:absolute;left:96px;top:0;width:1008px;height:53px;display:flex;align-items:center;justify-content:space-between;padding:0 10px}
.main-nav a{font-family:"Cabin",sans-serif;font-size:16px;color:var(--text-grey);text-decoration:none;padding:0 8px;line-height:53px}
.main-nav a.active{background:linear-gradient(180deg,var(--blue-light),var(--blue-deep));color:var(--white);padding:0 14px}
.language-tab{position:absolute;left:0;top:163px;width:29px;height:173px;background:var(--red);display:flex;align-items:center;justify-content:center}
.language-tab span{transform:rotate(-90deg);white-space:nowrap;color:var(--white);font-family:"Cabin",sans-serif;font-size:11px;letter-spacing:1px;font-weight:600}
.hero{position:absolute;left:96px;top:84px;width:1008px;height:336px;background:radial-gradient(ellipse at 60% 40%,var(--slide-a),var(--slide-b));border:1px solid #c3c8cd}
.hero-title{position:absolute;left:108px;top:52px;font-family:"Cabin",sans-serif;font-size:29px;color:var(--blue);font-weight:400}
.hero-text{position:absolute;left:108px;top:99px;width:290px;font-size:14px;line-height:17px;color:var(--blue)}
.hero-image{position:absolute;left:444px;top:22px;width:420px;height:300px;border-radius:50% 50% 40% 40%;background:radial-gradient(ellipse at 50% 38%,#e6e3b4 0,#cfcb8e 38%,#a7bfd3 62%,rgba(190,200,210,0) 75%)}
.hero-arrow{position:absolute;top:140px}
.hero-arrow.prev{left:20px}.hero-arrow.next{right:20px}
.panel{position:absolute;left:96px;top:432px;width:1008px;height:300px;background:var(--red);display:grid;grid-template-columns:240px 252px 252px 264px;box-shadow:0 2px 6px rgba(0,0,0,.3)}
.panel-col{position:relative;padding:20px 18px 0;border-left:1px solid var(--red-line)}
.panel-col:first-child{border-left:none}
.col-head{display:flex;align-items:flex-start;gap:10px;height:52px}
.col-icon{width:34px;height:34px;flex:none}
.col-title{font-family:"Cabin",sans-serif;font-size:20px;line-height:20px;color:var(--white);font-weight:400}
.col-title.small{font-size:17px;line-height:18px}
.portrait{width:36px;height:40px;background:linear-gradient(180deg,#cfd3d8,#3b4652);flex:none}
.about-text{font-size:11px;line-height:14px;color:#f1d9da;margin-top:6px}
.about-text p{margin-bottom:12px}
.entry{margin-bottom:14px}
.entry h3{font-family:"Cabin",sans-serif;font-size:12px;font-weight:700;color:var(--white);letter-spacing:.3px}
.entry p{font-size:11px;line-height:13px;color:#f1d9da}
.panel-btn{position:absolute;bottom:10px;right:18px;background:var(--red-dark);color:var(--white);font-family:"Cabin",sans-serif;font-size:13px;font-weight:600;padding:9px 16px;text-decoration:none}
.site-footer{position:absolute;left:106px;top:752px;width:990px;color:var(--white);font-size:12px}
.footer-links a{color:var(--white);text-decoration:none}
.footer-links span{margin:0 6px}
.copyright{margin-top:8px}
.flags{position:absolute;right:0;top:2px;display:flex;gap:8px}
.flag{width:16px;height:11px;display:flex}
.flag i{flex:1}
</style>
</head>
<body>
<nav class="main-nav">
  <a href="#">Biografia</a><a href="#">Libri</a><a href="#" class="active">Pubblicazioni scientifiche</a><a href="#">Conferenze</a><a href="#">Attività didattica</a><a href="#">Attività medica</a><a href="#">News</a><a href="#">Link</a><a href="#">Contatti</a>
</nav>

<div class="language-tab"><span>SELECT YOUR LANGUAGE</span></div>

<section class="hero">
  <h1 class="hero-title">Prof. Benedetto L. Caramuzza</h1>
  <p class="hero-text">Vivamus consectetur sem at dolor imperdiet non molestie magna ullamcorper. Praesent tempus, nunc sed ullamcorper gravida, orci justo rhoncus nisi, at adipiscing metus dolor eget nunc.</p>
  <div class="hero-image" role="img" aria-label="Photo of a model human brain held in two open hands"></div>
  <svg class="hero-arrow prev" width="22" height="44" viewBox="0 0 22 44"><polyline points="18,4 4,22 18,40" fill="none" stroke="#9aa1a8" stroke-width="4"/></svg>
  <svg class="hero-arrow next" width="22" height="44" viewBox="0 0 22 44"><polyline points="4,4 18,22 4,40" fill="none" stroke="#9aa1a8" stroke-width="4"/></svg>
</section>

<section class="panel">
  <div class="panel-col about">
    <div class="col-head"><div class="portrait" role="img" aria-label="Portrait of the professor"></div><h2 class="col-title">ABOUT<br>THE PROFESOR</h2></div>
    <div class="about-text">
      <p>Sed eget purus lacus, lobortis tempus nisl. Integer non lacus lacus. Morbi porttitor est quis purus facilisis mollis.</p>
      <p>Duis commodo mollis lacinia. Fusce blandit fermentum quam ut viverra. Mauris ut eleifend diam. Suspendisse aliquet, tortor at tempus porttitor, ipsum tortor tempor, ac congue mauris est a elit.</p>
    </div>
    <a href="#" class="panel-btn">READ MORE</a>
  </div>
  <div class="panel-col">
    <div class="col-head"><svg class="col-icon" viewBox="0 0 34 34"><rect x="5" y="3" width="22" height="28" fill="#fff"/><rect x="8" y="3" width="2" height="28" fill="#d9d9d9"/></svg><h2 class="col-title">LIBRI</h2></div>
    <div class="entry"><h3>FUSCE EU ORCI QUIS LIBERO SAGITTI</h3><p>Maecenas ac velit nec massa ultricies luctus ut non ante nec purus justo.</p></div>
    <div class="entry"><h3>VIVAMUS VESTIBULUM</h3><p>Maecenas ac velit nec massa ultricies luctus ut non ante nec purus justo.</p></div>
    <div class="entry"><h3>UT POSUERE FERMENTUM PULVINAR</h3><p>Maecenas ac velit nec massa ultricies luctus ut non ante nec purus justo.</p></div>
    <a href="#" class="panel-btn">SEE ALL</a>
  </div>
  <div class="panel-col">
    <div class="col-head"><svg class="col-icon" viewBox="0 0 34 34"><rect x="2" y="5" width="20" height="14" rx="3" fill="#fff"/><rect x="12" y="13" width="20" height="14" rx="3" fill="#d6d6d6"/></svg><h2 class="col-title">CONFERENZE</h2></div>
    <div class="entry"><h3>DONEC SCELERISQUE JUSTO EU</h3><p>Maecenas ac velit nec massa ultricies luctus ut non ante nec purus justo.</p></div>
    <div class="entry"><h3>SUSPENDISSE ALIQUET</h3><p>Maecenas ac velit nec massa ultricies luctus ut non ante nec purus justo.</p></div>
    <div class="entry"><h3>CRAS DICTUM ADIPISCING BIBEND</h3><p>Maecenas ac velit nec massa ultricies luctus ut non ante nec purus justo.</p></div>
    <a href="#" class="panel-btn">SEE ALL</a>
  </div>
  <div class="panel-col">
    <div class="col-head"><svg class="col-icon" viewBox="0 0 34 34"><rect x="6" y="2" width="22" height="30" fill="#fff"/><rect x="10" y="8" width="14" height="2" fill="#bbb"/><rect x="10" y="13" width="14" height="2" fill="#bbb"/><rect x="10" y="18" width="10" height="2" fill="#bbb"/></svg><h2 class="col-title small">PUBBLICAZIONI<br>SCIENTIFICHE</h2></div>
    <div class="entry"><h3>DONEC SCELERISQUE JUSTO EU</h3><p>Velit nec massa ultricies luctus.</p></div>
    <div class="entry"><h3>SUSPENDISSE ALIQUET</h3><p>Maecenas ac velit nec massa ultricies luctus ut non ante nec purus justo.</p></div>
    <div class="entry"><h3>CRAS DICTUM ADIPISCING BIBEND</h3><p>Maecenas ac velit nec massa ultricies luctus ut non ante nec purus justo.</p></div>
    <a href="#" class="panel-btn">SEE ALL</a>
  </div>
</section>

<footer class="site-footer">
  <div class="footer-links"><a href="#">Biografia</a><span>|</span><a href="#">Libri</a><span>|</span><a href="#">Pubblicazioni scientifiche</a><span>|</span><a href="#">Conferenze</a><span>|</span><a href="#">Attività didattica</a><span>|</span><a href="#">Attività medica</a><span>|</span><a href="#">News</a><span>|</span><a href="#">Link</a><span>|</span><a href="#">Contatti</a></div>
  <div class="copyright">Prof. Benedetto L. Caramuzza © All Rights Reserved 2011.</div>
  <div class="flags">
    <div class="flag"><i style="background:#2e9a48"></i><i style="background:#fff"></i><i style="background:#c8262e"></i></div>
    <div class="flag"><i style="background:#2a3f8a"></i><i style="background:#c8262e"></i><i style="background:#2a3f8a"></i></div>
  </div>
</footer>
</body>
</html>
```